Summit Grading a Builders LLC business card

My current business card is very plain. it has my logo and contact information. I woud like something that stands out from the rest. please take a look at my website to see about my company.

Compayt Name - Summit Grading And Builders
Owner - Martin Kowalczyk
Business Address
Business Website - www.summitgradingandbuilders.example
Email - Summitgradingandbuilders@mailbox.example
Phone - 555-214-7390
Fax - 555-806-3127

Target Market(s)

Everyone age tang is 18 - 85

Industry/Entity Type

Business

Contact Information for Business Card

Nice and professional all in one.

Font styles to use
Serif
Other font styles liked:
• Up to you

Requirements
Must have
• All contact info. The design is up to you.
Nice to have
• All the contact info the design is up to you
Should not have
• I don't have any

```html
<!DOCTYPE html>
<html lang="en">
<head>
<meta charset="utf-8">
<title>Summit Grading &amp; Builders LLC – Business Card</title>
<link rel="stylesheet" href="https://fonts.googleapis.com/css2?family=EB+Garamond:wght@400;600&display=swap">
<style>
  :root {
    --page-bg: #e9e8e4;
    --card-front: #f2f2f2;
    --card-back: #444444;
    --ink-dark: #2b2b2b;
    --ink-green: #2f7d2a;
    --divider: #555555;
    --back-mark: #575757;
  }
  * { margin: 0; padding: 0; box-sizing: border-box; }
  html, body { width: 1200px; height: 1000px; overflow: hidden; }
  body {
    background: var(--page-bg);
    font-family: "EB Garamond", Georgia, serif;
    position: relative;
  }
  .card {
    position: absolute;
    width: 646px;
    height: 348px;
    box-shadow: 0 6px 14px rgba(0,0,0,0.18);
  }
  .card-front {
    left: 110px; top: 150px;
    background: var(--card-front);
  }
  .card-back {
    left: 444px; top: 520px;
    background: var(--card-back);
    display: flex; align-items: center; justify-content: center;
  }
  .brand-name {
    position: absolute;
    left: 36px; top: 132px;
    width: 260px;
    text-align: center;
    font-size: 31px;
    line-height: 1.05;
    font-weight: 600;
    text-transform: uppercase;
    color: var(--ink-dark);
    letter-spacing: 0.5px;
  }
  .divider {
    position: absolute;
    left: 303px; top: 98px;
    width: 2px; height: 154px;
    background: var(--divider);
  }
  .owner {
    position: absolute;
    left: 340px; top: 114px;
    width: 200px;
    text-align: center;
    color: var(--ink-green);
  }
  .owner-name { font-size: 20px; line-height: 1.1; }
  .owner-title { font-size: 14px; line-height: 1.1; }
  .contact-list {
    position: absolute;
    left: 320px; top: 154px;
    list-style: none;
    color: var(--ink-green);
    font-size: 11.5px;
  }
  .contact-item {
    display: flex; align-items: center;
    height: 19.5px;
  }
  .contact-item svg { width: 17px; height: 17px; margin-right: 10px; flex: none; }
  .back-name {
    font-size: 40px;
    line-height: 1.05;
    font-weight: 600;
    text-transform: uppercase;
    color: var(--back-mark);
    text-align: center;
    letter-spacing: 1px;
  }
</style>
</head>
<body>
  <section class="card card-front" aria-label="Business card front">
    <div class="brand-name">Summit Grading &amp; Builders LLC</div>
    <div class="divider"></div>
    <div class="owner">
      <div class="owner-name">Martin Kowalczyk</div>
      <div class="owner-title">Owner</div>
    </div>
    <ul class="contact-list">
      <li class="contact-item">
        <svg viewBox="0 0 20 20"><circle cx="10" cy="10" r="9" fill="var(--ink-green)"/><path d="M6.5 5.5l2 0 1 2.5-1.3 1c.6 1.3 1.5 2.2 2.8 2.8l1-1.3 2.5 1v2c0 .6-.5 1-1 1C9 14.5 5.5 11 5.5 6.5c0-.5.4-1 1-1z" fill="#fff"/></svg>
        <span>555-214-7390</span>
      </li>
      <li class="contact-item">
        <svg viewBox="0 0 20 20"><rect x="3" y="8" width="14" height="9" rx="1" fill="var(--ink-green)"/><rect x="6" y="3" width="8" height="6" fill="var(--ink-green)"/><rect x="7" y="4" width="6" height="4" fill="#fff"/><rect x="6" y="11" width="8" height="1.4" fill="#fff"/><rect x="6" y="13.6" width="8" height="1.4" fill="#fff"/></svg>
        <span>555-806-3127</span>
      </li>
      <li class="contact-item">
        <svg viewBox="0 0 20 20"><path d="M10 2a6 6 0 0 0-6 6c0 4.5 6 10 6 10s6-5.5 6-10a6 6 0 0 0-6-6z" fill="var(--ink-green)"/><circle cx="10" cy="8" r="2.2" fill="#fff"/></svg>
        <span>418 Ridge Avenue, Millbrook, NY, United States</span>
      </li>
      <li class="contact-item">
        <svg viewBox="0 0 20 20"><rect x="2" y="5" width="16" height="11" fill="var(--ink-green)"/><path d="M2.5 5.5L10 11l7.5-5.5" stroke="#fff" stroke-width="1.3" fill="none"/></svg>
        <span>Summitgradingandbuilders@mailbox.example</span>
      </li>
      <li class="contact-item">
        <svg viewBox="0 0 20 20"><circle cx="10" cy="10" r="8" fill="var(--ink-green)"/><g stroke="#fff" stroke-width="1" fill="none"><ellipse cx="10" cy="10" rx="3.5" ry="7.5"/><path d="M2.5 10h15M4 6h12M4 14h12M10 2.5v15"/></g></svg>
        <span>www.summitgradingandbuilders.example</span>
      </li>
    </ul>
  </section>

  <section class="card card-back" aria-label="Business card back">
    <div class="back-name">Summit Grading<br>&amp; Builders LLC</div>
  </section>
</body>
</html>
```